Drag Show Flyer

We are holding a Drag Show, we are looking for something fun and exciting, over the top is a must.

Show Date: Saturday September 2nd 2017
Venue: Pelican Row Cafe Bunbury
Doors open 7pm
Tickets: $50 per person, includes glass of sparkling on arrival and canapes
Tickets available at the Venue or from ticketloom.com.au

Target Market(s)

Female, Hens Party, LBGT

Industry/Entity Type

Entertainment

Colors

Designer to choose colors to be used in the design.

Requirements
Must have
• Show Date: Saturday September 2nd 2017
• Venue: Pelican Row Cafe Bunbury
• Doors open 7pm
• Tickets: $50 per person, includes glass of sparkling on arrival and canapes
• Tickets available at the Venue or from ticketloom.com.au

```html
<!DOCTYPE html>
<html lang="en">
<head>
<meta charset="utf-8">
<title>Drag Show Night 2017</title>
<link rel="stylesheet" href="https://fonts.googleapis.com/css2?family=Montserrat:wght@300;400;600;700;800&family=Oswald:wght@600;700&family=Russo+One&display=swap">
<style>
  :root {
    --paper: #fbfbfb;
    --ink: #141414;
    --olive: #cdc62a;
    --pill: #f7e27c;
    --pill-dot: #d8cd2c;
    --gold-1: #fff1b8;
    --gold-2: #c9a64a;
    --gold-3: #7d5e1c;
    --band: #111111;
    --brown: #5b3a33;
    --pink: #ec2f8a;
    --red: #c8102e;
    --orange: #f08a1c;
    --yellow: #f5d31c;
  }
  * { box-sizing: border-box; margin: 0; padding: 0; }
  html, body { width: 878px; height: 1200px; overflow: hidden; }
  body { background: var(--paper); font-family: "Montserrat", sans-serif; color: var(--ink); }
  .flyer { position: relative; width: 878px; height: 1200px; overflow: hidden; background: var(--paper); }

  .hero-art { position: absolute; left: 0; top: 0; width: 878px; height: 840px; }
  .corner-shapes { position: absolute; left: 0; top: 0; width: 878px; height: 900px; pointer-events: none; }

  .title-drag {
    position: absolute; left: 192px; top: 344px; width: 540px; text-align: center;
    font-family: "Russo One", sans-serif; font-size: 122px; line-height: 1; letter-spacing: 2px;
    background: linear-gradient(180deg, #ffffff 0%, #bdbdbd 45%, #f2f2f2 60%, #8d8d8d 100%);
    -webkit-background-clip: text; background-clip: text; color: transparent;
    filter: drop-shadow(0 3px 3px rgba(0,0,0,.6));
  }
  .title-show {
    position: absolute; left: 192px; top: 456px; width: 540px; text-align: center;
    font-family: "Russo One", sans-serif; font-size: 124px; line-height: 1; letter-spacing: 2px;
    color: #ffffff;
    text-shadow: 0 0 6px #fff, 0 0 16px rgba(255,240,200,.9), 0 0 30px rgba(255,200,120,.6);
  }
  .title-night-box { position: absolute; left: 194px; top: 594px; width: 494px; height: 114px; background: rgba(20,14,10,.55); }
  .title-night {
    position: absolute; left: 206px; top: 604px;
    font-family: "Montserrat", sans-serif; font-weight: 800; font-size: 98px; line-height: 1; letter-spacing: 1px;
    background: linear-gradient(180deg, var(--gold-1) 0%, var(--gold-2) 50%, var(--gold-3) 70%, var(--gold-1) 100%);
    -webkit-background-clip: text; background-clip: text; color: transparent;
  }
  .title-year {
    position: absolute; left: 636px; top: 654px; transform: translate(-50%, -50%) rotate(-90deg);
    font-weight: 800; font-size: 42px; color: #ffffff; line-height: 1;
  }

  .date { position: absolute; left: 138px; top: 774px; }
  .date-day { font-weight: 700; font-size: 37px; line-height: 1; letter-spacing: .5px; }
  .date-num { font-weight: 700; font-size: 96px; line-height: .9; color: var(--olive); margin-top: 6px; }
  .date-month { font-weight: 700; font-size: 37px; line-height: 1; margin-top: 4px; letter-spacing: .5px; }
  .date-year {
    position: absolute; left: 428px; top: 860px; transform: translate(-50%, -50%) rotate(-90deg);
    font-weight: 300; font-size: 66px; color: var(--brown); line-height: 1; letter-spacing: 1px;
  }

  .venue-pill { position: absolute; left: 460px; top: 845px; width: 372px; height: 58px; border-radius: 29px; background: var(--pill); }
  .venue-at {
    position: absolute; left: 0; top: -5px; width: 68px; height: 68px; border-radius: 50%;
    background: var(--pill-dot); font-weight: 800; font-size: 40px; line-height: 60px; text-align: center;
  }
  .venue-name { position: absolute; left: 78px; top: 5px; font-weight: 700; font-size: 24px; line-height: 1.08; letter-spacing: .6px; }
  .venue-doors { position: absolute; left: 538px; top: 912px; font-weight: 600; font-size: 16px; letter-spacing: 1px; color: var(--ink); }

  .ticket-band { position: absolute; left: 0; top: 944px; width: 878px; height: 92px; background: var(--band); }
  .ticket-label {
    position: absolute; left: 120px; top: 990px; transform: translate(-50%, -50%) rotate(-90deg);
    font-weight: 600; font-size: 16px; color: #fff; letter-spacing: .5px;
  }
  .ticket-price {
    position: absolute; left: 144px; top: 950px;
    font-family: "Oswald", sans-serif; font-weight: 700; font-size: 70px; line-height: 1;
    background: linear-gradient(180deg, var(--gold-1), var(--gold-2) 55%, var(--gold-3));
    -webkit-background-clip: text; background-clip: text; color: transparent;
  }
  .ticket-per { position: absolute; left: 265px; top: 960px; font-size: 29px; line-height: 1.02; color: var(--pill); letter-spacing: 1px; }
  .ticket-divider { position: absolute; left: 408px; top: 968px; width: 1px; height: 44px; background: var(--gold-2); }
  .ticket-includes { position: absolute; left: 420px; top: 966px; width: 418px; text-align: center; color: #fff; font-size: 19px; line-height: 1.45; letter-spacing: .3px; }

  .ticket-source { position: absolute; left: 111px; top: 1058px; display: flex; align-items: baseline; gap: 12px; }
  .ticket-source-note { font-size: 16px; }
  .ticket-source-url { font-size: 38px; font-weight: 400; color: var(--olive); letter-spacing: 1px; }

  .partners { position: absolute; left: 0; top: 1098px; width: 878px; height: 86px; }
  .partner { position: absolute; top: 0; height: 86px; display: flex; align-items: center; gap: 10px; font-weight: 700; font-size: 14px; line-height: 1.2; color: var(--ink); }
  .partner-mark { width: 26px; height: 26px; border-radius: 50%; flex: none; }
  .partner-one { left: 160px; width: 160px; }
  .partner-one .partner-mark { background: var(--pink); }
  .partner-two { left: 340px; width: 176px; top: 12px; height: 62px; justify-content: center; background: var(--band); color: #fff; }
  .partner-three { left: 574px; width: 180px; }
  .partner-three .partner-mark { background: var(--ink); width: 40px; height: 40px; }
</style>
</head>
<body>
<main class="flyer">

  <svg class="hero-art" viewBox="0 0 878 840" role="img" aria-label="Photo collage of a glamorous performer in bold sunglasses with a concert crowd and stage lights, set in a painted splash">
    <defs>
      <linearGradient id="heroTone" x1="0" y1="0" x2="1" y2="1">
        <stop offset="0" stop-color="#b8243a"/>
        <stop offset=".3" stop-color="#5a4a2c"/>
        <stop offset=".5" stop-color="#2c3a6e"/>
        <stop offset=".72" stop-color="#8a4a1e"/>
        <stop offset="1" stop-color="#e8a02a"/>
      </linearGradient>
      <radialGradient id="heroGlow" cx=".55" cy=".72" r=".45">
        <stop offset="0" stop-color="#ffe6a0" stop-opacity=".75"/>
        <stop offset="1" stop-color="#ffe6a0" stop-opacity="0"/>
      </radialGradient>
    </defs>
    <path d="M20 40 L120 0 L760 0 L830 30 L860 120 L850 220 L870 300 L845 400 L858 520 L836 640 L862 760 L800 790 L720 760 L640 800 L540 770 L450 790 L380 740 L300 770 L210 720 L130 690 L60 640 L20 560 L0 460 L14 340 L0 220 Z" fill="url(#heroTone)"/>
    <path d="M20 40 L120 0 L760 0 L830 30 L860 120 L850 220 L870 300 L845 400 L858 520 L836 640 L862 760 L800 790 L720 760 L640 800 L540 770 L450 790 L380 740 L300 770 L210 720 L130 690 L60 640 L20 560 L0 460 L14 340 L0 220 Z" fill="url(#heroGlow)"/>
  </svg>

  <svg class="corner-shapes" viewBox="0 0 878 900" aria-hidden="true">
    <polygon points="0,0 44,0 0,50" fill="var(--red)"/>
    <polygon points="706,34 744,28 720,56" fill="#7a0c1c"/>
    <polygon points="620,0 650,0 636,14" fill="var(--red)"/>
    <polygon points="858,0 878,0 878,40" fill="var(--red)"/>
    <polygon points="38,744 52,734 52,764" fill="var(--orange)"/>
    <polygon points="0,800 36,812 0,832" fill="var(--yellow)"/>
    <polygon points="86,830 110,816 110,870" fill="var(--orange)"/>
  </svg>

  <h1 class="title">
    <span class="title-drag">DRAG</span>
    <span class="title-show">SHOW</span>
    <span class="title-night-box"></span>
    <span class="title-night">NIGHT</span>
    <span class="title-year">2017</span>
  </h1>

  <div class="date">
    <div class="date-day">SATURDAY</div>
    <div class="date-num">2ND</div>
    <div class="date-month">SEPTEMBER</div>
  </div>
  <div class="date-year">2017</div>

  <div class="venue-pill">
    <span class="venue-at">at</span>
    <span class="venue-name">Pelican Row Cafe<br>Bunbury</span>
  </div>
  <p class="venue-doors">DOORS OPEN 7PM</p>

  <section class="ticket-band"></section>
  <span class="ticket-label">TICKETS:</span>
  <span class="ticket-price">$50</span>
  <span class="ticket-per">Per<br>Person</span>
  <span class="ticket-divider"></span>
  <p class="ticket-includes">INCLUDES GLASS OF SPARKLING ON<br>ARRIVAL AND CANAPES</p>

  <p class="ticket-source">
    <span class="ticket-source-note">Tickets available at the Venue or from</span>
    <span class="ticket-source-url">ticketloom.com.au</span>
  </p>

  <footer class="partners">
    <div class="partner partner-one"><span class="partner-mark"></span><span>Loud Lips<br>Productions</span></div>
    <div class="partner partner-two">Pelican Row</div>
    <div class="partner partner-three"><span class="partner-mark"></span><span>The Velvet<br>Group</span></div>
  </footer>

</main>
</body>
</html>
```